Petal Sprite - web design for my new flower atelier

I would like to ask for design proposal for my newly established flower atelier. My brand name is Petal Sprite and I focus on realisation of events and flower projects (any kind) for physical as well as legel persons. I don’t operate as a standard flowershop. I would like to have 5 key parts - 1/Landing pg/welcome, 2/About me, 3/Gallery, 4/References, 5/Contact details. I would like the web design to reflect the way I am/ I do the things, ie, be slightly different, do non-tradiotional arrangements, my passion for flowers, gentle& fregile style, love for minimalism and details in the arrangements. I attach couple of photos of what I do so that you can better understand my style . You can see more on IG mirka_petal_sprite or FB Petal Sprite. I was wondering maybe one of the first 2 photos could be part of the landing pg. Or another idea is to have a design similar to this one https://thistlebloomstudio.example, ie to choose 3-5photos which are being animated like here. However, I am open to discuss any ideas and look forward for all the proposals.

Target Market(s)

physical as well as legal persons - weddings, celebrations, business events, projects for hotels, beaty salons, restaurants and others.. actually any kind of flower project

Industry/Entity Type

flowers

Number of Pages Required

1 page

Font styles to use
Other font styles liked:
• the font which matches the logo font style

Requirements
Must have
• to reflect the way I am as described above, I prefer more simple way of design, with the attention to a detail, I prefer pastel colours

```html
<!DOCTYPE html>
<html lang="en">
<head>
<meta charset="utf-8">
<title>Petal Sprite — Flower Atelier</title>
<link href="https://fonts.googleapis.com/css2?family=Great+Vibes&family=Parisienne&family=Karla:wght@400;500&display=swap" rel="stylesheet">
<style>
:root{
  --cream:#fdf7f0;
  --sand:#f8efe6;
  --badge:#f7ece3;
  --brown:#7a5634;
  --brown-soft:#8f6a48;
  --line:#8a6442;
  --green:#6f9440;
  --white:#ffffff;
  --card-band:#f6ede4;
}
*{box-sizing:border-box;margin:0;padding:0}
html,body{width:1200px;height:3148px;overflow:hidden}
body{position:relative;background:var(--white);font-family:"Karla",sans-serif;color:var(--brown)}
.abs{position:absolute}
.script{font-family:"Great Vibes",cursive;font-weight:400;color:var(--brown)}
.brand{font-family:"Karla",sans-serif;font-weight:500;color:var(--brown);letter-spacing:1px}

/* hero */
.hero{left:0;top:0;width:1200px;height:599px;background:linear-gradient(180deg,#eeeeed 0%,#e6e6e5 100%)}
.hero-photo{left:574px;top:0;width:538px;height:580px;background:linear-gradient(180deg,#dfe5cf 0%,#d8dcc9 45%,#cfc8bd 75%,#c6bbae 100%)}
.badge{left:181px;top:159px;width:387px;height:281px}
.badge-name{left:181px;top:242px;width:387px;text-align:center;font-size:22px}
.badge-mark{left:354px;top:184px;width:42px;height:42px;border:1px solid var(--line);border-radius:50%}
.badge-rule{left:247px;top:293px;width:255px;border-top:1px solid var(--line)}
.badge-text{left:256px;top:312px;width:244px;text-align:center;font-size:11.5px;line-height:16px;color:#4a3a2c}
.badge-scroll{left:324px;top:384px;width:100px;text-align:center;font-size:10.5px;line-height:13px;color:#4a3a2c}

/* nav */
.nav{left:0;top:599px;width:1200px;height:46px;background:var(--white)}
.nav a{position:absolute;top:17px;font-size:10px;letter-spacing:2px;text-transform:uppercase;color:var(--brown-soft);text-decoration:none;transform:translateX(-50%)}

/* headings */
.heading{left:0;width:1200px;text-align:center;font-size:56px;line-height:60px}
.rule{border-top:1.5px solid var(--line)}

/* welcome */
.welcome{left:0;top:645px;width:1200px;height:641px;background:var(--cream)}
.welcome-box{left:225px;top:810px;width:749px;height:416px;border:1px solid var(--brown-soft);background:var(--white)}
.welcome-mark{left:576px;top:872px;width:48px;height:48px;border:1px solid var(--line);border-radius:50%}
.welcome-name{left:0;top:928px;width:1200px;text-align:center;font-size:22px}
.tagline{left:0;top:976px;width:1200px;text-align:center;font-family:"Parisienne",cursive;font-size:19px;line-height:23px;color:var(--brown-soft)}
.welcome-text{left:350px;top:1047px;width:500px;text-align:center;font-size:12.5px;line-height:22.5px;color:var(--brown-soft)}
.btn{left:544px;top:1152px;width:112px;height:29px;background:var(--green);color:var(--white);font-size:11px;line-height:29px;text-align:center}

/* services */
.services-text{left:262px;top:1460px;width:676px;text-align:center;font-size:12.5px;line-height:18px;letter-spacing:.3px;color:var(--brown-soft)}
.card{top:1569px;width:210px;height:313px;border:1px solid #e3d7ca;background:var(--card-band)}
.card-photo{position:absolute;left:0;top:0;width:208px;height:260px}
.card-label{position:absolute;left:0;top:260px;width:208px;height:51px;line-height:51px;text-align:center;font-size:12px;letter-spacing:.8px;color:var(--brown);text-transform:uppercase}

/* gallery */
.gallery{left:0;top:1943px;width:1200px;height:859px;background:var(--cream)}
.tile{border:1px solid #e3dbd2}
.view-more{background:var(--white);color:var(--green);font-size:11px;display:flex;align-items:center;justify-content:center}

/* footer */
.footer{left:0;top:2802px;width:1200px;height:346px;background:var(--sand)}
.foot-head{font-family:"Parisienne",cursive;font-size:20px;color:var(--green)}
.foot-link{left:214px;font-size:11px;color:var(--brown-soft)}
.foot-box{left:431px;top:2863px;width:338px;height:224px;background:var(--white);border:1px solid var(--brown-soft)}
.foot-mark{left:580px;top:2898px;width:40px;height:40px;border:1px solid var(--line);border-radius:50%}
.foot-name{left:431px;top:2950px;width:338px;text-align:center;font-size:19px}
.foot-rule{left:473px;top:3002px;width:254px;border-top:1px solid var(--line)}
.social{top:3022px;width:37px;height:37px;background:var(--card-band)}
.contact-text{left:907px;font-size:11px;line-height:20px;letter-spacing:.4px;color:var(--brown-soft)}
</style>
</head>
<body>

<!-- hero -->
<section class="abs hero" role="img" aria-label="Soft grey textured studio backdrop"></section>
<div class="abs hero-photo" role="img" aria-label="Photograph of pale green hellebores and foliage in a bronze vase"></div>

<svg class="abs badge" viewBox="0 0 387 281" aria-hidden="true">
  <path d="M193 6 C240 6 260 30 300 30 C350 30 381 60 381 110 L381 175 C381 225 350 250 300 250 C260 250 240 275 193 275 C146 275 126 250 86 250 C36 250 6 225 6 175 L6 110 C6 60 36 30 86 30 C126 30 146 6 193 6 Z" fill="#f6e8dd"/>
  <path d="M193 14 C238 14 258 38 298 38 C344 38 373 66 373 112 L373 173 C373 219 344 242 298 242 C258 242 238 267 193 267 C148 267 128 242 88 242 C42 242 14 219 14 173 L14 112 C14 66 42 38 88 38 C128 38 148 14 193 14 Z" fill="var(--badge)" stroke="var(--line)" stroke-width="1"/>
</svg>
<div class="abs badge-mark"></div>
<div class="abs badge-name brand">Petal Sprite</div>
<div class="abs badge-rule"></div>
<p class="abs badge-text">Lorem ipsum dolor sit amet, consectetur adipiscing elit, sed do eiusmod tempor incididunt ut labore et dolore</p>
<div class="abs badge-scroll">Scroll to<br>Experience
  <svg width="10" height="7" viewBox="0 0 10 7" style="display:block;margin:2px auto 0"><path d="M1 1 L5 5 L9 1" fill="none" stroke="#4a3a2c" stroke-width="1.2"/></svg>
</div>

<!-- navigation -->
<nav class="abs nav">
  <a style="left:400px">Home</a>
  <a style="left:481px">Events</a>
  <a style="left:572px">Gallery</a>
  <a style="left:670px">About Us</a>
  <a style="left:778px">Contact Us</a>
</nav>

<!-- welcome -->
<section class="abs welcome"></section>
<div class="abs rule" style="left:337px;top:727px;width:169px"></div>
<div class="abs rule" style="left:692px;top:727px;width:171px"></div>
<h2 class="abs heading script" style="top:698px">Welcome</h2>

<div class="abs welcome-box"></div>
<div class="abs welcome-mark"></div>
<div class="abs welcome-name brand">Petal Sprite</div>
<p class="abs tagline">Special event florist for all types<br>of Events and Projects</p>
<p class="abs welcome-text">Lorem ipsum dolor sit amet, consectetur adipiscing elit, sed do eiusmod tempor incididunt ut labore et dolore magna aliqua. Quis ipsum suspendisse ultrices gravida. Risus commodo viverra maecenas accumsan lacus vel facilisis.</p>
<div class="abs btn">Learn More</div>

<!-- services -->
<div class="abs rule" style="left:337px;top:1376px;width:124px"></div>
<div class="abs rule" style="left:737px;top:1376px;width:126px"></div>
<h2 class="abs heading script" style="top:1344px">Our Services</h2>
<p class="abs services-text">Lorem ipsum dolor sit amet, consectetur adipiscing elit, sed do eiusmod tempor incididunt ut labore et dolore magna aliqua. Quis ipsum suspendisse ultrices gravida. Risus commodo viverra maecenas accumsan lacus vel facilisis.</p>

<div class="abs card" style="left:187px">
  <div class="card-photo" role="img" aria-label="Photograph of a hand holding a yellow and peach wedding bouquet" style="background:linear-gradient(180deg,#8f897b 0%,#b9ab88 55%,#cfae8e 100%)"></div>
  <div class="card-label">Weddings</div>
</div>
<div class="abs card" style="left:495px">
  <div class="card-photo" role="img" aria-label="Photograph of red and white ranunculus on a cork side table by a yellow chair" style="background:linear-gradient(180deg,#c9a24a 0%,#d8b25a 55%,#c9ab8c 100%)"></div>
  <div class="card-label">Events</div>
</div>
<div class="abs card" style="left:803px">
  <div class="card-photo" role="img" aria-label="Photograph of curly branches and small yellow blooms in a dark green vase" style="background:linear-gradient(180deg,#e4e4e2 0%,#d6d8d2 100%)"></div>
  <div class="card-label">Projects</div>
</div>

<!-- gallery -->
<section class="abs gallery"></section>
<div class="abs rule" style="left:337px;top:2035px;width:172px"></div>
<div class="abs rule" style="left:692px;top:2035px;width:171px"></div>
<h2 class="abs heading script" style="top:2003px">Gallery</h2>

<div class="abs tile" style="left:187px;top:2129px;width:404px;height:403px;background:linear-gradient(180deg,#a8a79f 0%,#c8c3a6 55%,#cfd3b0 100%)" role="img" aria-label="Photograph of orange and yellow poppies in a green glass vase"></div>
<div class="abs tile" style="left:607px;top:2129px;width:405px;height:193px;background:linear-gradient(180deg,#e6e4e1 0%,#c7ae98 100%)" role="img" aria-label="Photograph of a long autumn arrangement with berries and dried twigs"></div>
<div class="abs tile" style="left:607px;top:2338px;width:195px;height:404px;background:linear-gradient(180deg,#a98270 0%,#d9ab98 50%,#cbb69c 100%)" role="img" aria-label="Photograph of peach tulips in a glass cylinder vase on a table"></div>
<div class="abs tile" style="left:817px;top:2338px;width:195px;height:194px;background:linear-gradient(180deg,#dce2d0 0%,#cfc7bd 100%)" role="img" aria-label="Photograph of green hellebores in a bronze vase"></div>
<div class="abs tile" style="left:187px;top:2548px;width:194px;height:194px;background:linear-gradient(180deg,#b3b8c0 0%,#c6ad92 100%)" role="img" aria-label="Photograph of a loose orange and white arrangement against patterned tiles"></div>
<div class="abs tile" style="left:397px;top:2548px;width:194px;height:194px;background:linear-gradient(180deg,#d6d6d4 0%,#c8c2bc 100%)" role="img" aria-label="Photograph of a cotton branch in a slim taupe vase"></div>
<div class="abs tile view-more" style="left:817px;top:2548px;width:195px;height:194px">View More</div>

<!-- footer -->
<footer class="abs footer"></footer>
<div class="abs foot-head" style="left:192px;top:2866px">Quick Links</div>
<div class="abs foot-link" style="top:2907px">Home</div>
<div class="abs foot-link" style="top:2934px">Booking</div>
<div class="abs foot-link" style="top:2961px">Portfolio</div>
<div class="abs foot-link" style="top:2988px">Contact</div>

<div class="abs foot-box"></div>
<div class="abs foot-mark"></div>
<div class="abs foot-name brand">Petal Sprite</div>
<div class="abs foot-rule"></div>
<div class="abs social" style="left:501px" aria-label="Instagram"></div>
<div class="abs social" style="left:582px" aria-label="Facebook"></div>
<div class="abs social" style="left:662px" aria-label="Pinterest"></div>

<div class="abs foot-head" style="left:924px;top:2866px">Contact</div>
<svg class="abs" style="left:879px;top:2916px" width="10" height="13" viewBox="0 0 10 13" aria-hidden="true"><path d="M5 12 C2 8 1 6 1 4.5 A4 4 0 0 1 9 4.5 C9 6 8 8 5 12 Z" fill="none" stroke="var(--brown)" stroke-width="1.2"/><circle cx="5" cy="4.5" r="1.4" fill="var(--brown)"/></svg>
<div class="abs contact-text" style="top:2904px">Lindenweg 42, Brookvale,<br>Meadowshire</div>
<svg class="abs" style="left:880px;top:2969px" width="12" height="12" viewBox="0 0 12 12" aria-hidden="true"><path d="M2.5 1 L4.5 1 L5.5 3.5 L4 4.7 C4.7 6.3 5.7 7.3 7.3 8 L8.5 6.5 L11 7.5 L11 9.5 C11 10.3 10.3 11 9.5 11 C5 11 1 7 1 2.5 C1 1.7 1.7 1 2.5 1 Z" fill="none" stroke="var(--brown)" stroke-width="1.1"/></svg>
<div class="abs contact-text" style="top:2966px">555 014 272</div>

</body>
</html>
```